velmorino.eu :: Design ideas (no coding) for key pages of Personalized greeting cards online store

We need your vision on modern, clean, easy to read user interface (UI) for online service of personalized printed products, like greeting cards, postcards, fridge magnets, clips and etc.
Your vision should include UI presentation for:
- Home page with login (including soc nets)
- Product Designer page
- Cart pages (products and address selection)
- Example of general internal page (pricing, terms, etc)
- Artist info and portfolio page
We are looking for ideas we will love, NOT complete design of a whole site.
Top design/vision will we used as a basement for separate contract on complete design of the site.

UI should be based on existing functionality with some extent. It should not break ideas or methods used on prototype but designers are free to offer own product presentations, designer’s layout and cart views.

Prototype:
English: http://velmorino.eu
Russian: http://velmorino.ru
Lithuanian: http://velmorino.lt

Target Market(s)

People of 16-45 y.o. who likes to be distinctive, personal.

Industry/Entity Type

Store

Requirements
Must have
• Your work should meet attached requirements.
Site is multilingual. Wording should assume varieties in length on different languages.
Clean and easy to read UI
Flat design preferrably
Should be based on assets which are free or available for royalty-free licensing
Should not have
• heavy, meaningless 3D and shadow effects
Show NOT copy sites like: plonkra.com, tarnwick.co.uk

```html
<!DOCTYPE html>
<html lang="en">
<head>
<meta charset="utf-8">
<title>velmorino.eu – Add Image</title>
<link href="https://fonts.googleapis.com/css2?family=Open+Sans:wght@400;600;700&family=Arimo:wght@700&display=swap" rel="stylesheet">
<style>
  :root {
    --checker-light: #8c8c8c;
    --checker-dark: #7b7b7b;
    --frame: #767676;
    --panel: #ffffff;
    --ink: #111111;
    --field-border: #c9c9c9;
    --field-text: #555555;
    --teal: #209792;
    --muted-btn: #c8c8c8;
    --muted-text: #7a7a7a;
    --crimson: #8e1b13;
  }
  * { box-sizing: border-box; margin: 0; padding: 0; }
  html, body { width: 1200px; height: 816px; overflow: hidden; }
  body {
    position: relative;
    font-family: "Open Sans", sans-serif;
    background-color: var(--checker-light);
    background-image: repeating-conic-gradient(var(--checker-dark) 0 25%, var(--checker-light) 0 50%);
    background-size: 14px 14px;
  }
  .modal {
    position: absolute;
    left: 423px; top: 135px;
    width: 354px; height: 548px;
    background: var(--panel);
    border: 9px solid var(--frame);
  }
  .close-btn {
    position: absolute;
    left: 769px; top: 92px;
    width: 45px; height: 45px;
    border-radius: 50%;
    background: var(--crimson);
    border: 4px solid #fff;
    color: #fff;
    font: 700 20px/35px "Open Sans", sans-serif;
    text-align: center;
  }
  .modal-title {
    position: absolute;
    left: 0; right: 0; top: 24px;
    display: flex; align-items: center; justify-content: center; gap: 6px;
    font-weight: 600; font-size: 30px; color: var(--ink); line-height: 40px;
  }
  .modal-title svg { display: block; }
  .browse-list { position: absolute; left: 32px; top: 102px; width: 273px; }
  .browse-field {
    display: flex; height: 47px; margin-bottom: 8px;
    border: 1px solid var(--field-border);
  }
  .browse-field span {
    flex: 1; padding-left: 14px;
    font-size: 16px; line-height: 45px; color: var(--field-text);
  }
  .browse-field b {
    width: 40px; margin: -1px -1px -1px 0;
    background: var(--muted-btn); color: #fff;
    font-size: 21px; line-height: 46px; text-align: center; font-weight: 700;
    border: 1px solid #b5b5b5;
  }
  .browse-field.active b { background: var(--teal); border-color: var(--teal); }
  .add-more {
    position: absolute; right: 31px; top: 283px;
    font-size: 11.5px; font-weight: 700; color: var(--muted-text);
  }
  .thumbs { position: absolute; left: 32px; top: 318px; display: flex; gap: 7px; }
  .thumb {
    position: relative;
    width: 86px; height: 80px;
    border: 1px solid #cfcfcf; border-radius: 2px;
    overflow: hidden;
  }
  .thumb svg { position: absolute; left: 31px; top: 28px; opacity: .55; }
  .thumb-foliage {
    border-color: #1d2a1f;
    background:
      radial-gradient(circle at 45% 88%, #49c36a 0 6%, transparent 22%),
      radial-gradient(ellipse at 0% 0%, #d99a4a 0 14%, transparent 32%),
      radial-gradient(ellipse at 70% 35%, #2e7a45, transparent 55%),
      linear-gradient(160deg, #1d5a31, #0b2e18 70%, #082414);
  }
  .thumb-cards {
    background:
      linear-gradient(180deg, transparent 0 62%, #6e5a44 62% 74%, transparent 74%),
      radial-gradient(ellipse at 55% 45%, #efe6d6 0 30%, transparent 48%),
      radial-gradient(ellipse at 80% 85%, #ece6de 0 18%, transparent 30%),
      linear-gradient(170deg, #e8ddc8, #cbb48e 60%, #a88e68);
  }
  .thumb-tree {
    background:
      radial-gradient(ellipse at 50% 38%, #9fb9ae 0 22%, #c7b4a5 34%, transparent 46%),
      linear-gradient(180deg, transparent 0 58%, #7a5a4c 58% 62%, transparent 62%),
      linear-gradient(160deg, #f0b7a6, #e6a896 55%, #efc2b2);
  }
  .actions { position: absolute; left: 31px; top: 449px; display: flex; gap: 4px; }
  .btn {
    height: 47px; border-radius: 2px; color: #fff;
    font: 700 20px/47px "Arimo", sans-serif; text-align: center;
  }
  .btn-cancel { width: 132px; background: var(--crimson); }
  .btn-ok { width: 138px; background: var(--teal); }
</style>
</head>
<body>
  <div class="close-btn">x</div>
  <section class="modal">
    <h1 class="modal-title">
      <svg width="42" height="12" viewBox="0 0 42 12"><line x1="0" y1="6" x2="32" y2="6" stroke="#111" stroke-width="1.2"/><circle cx="36" cy="6" r="4" fill="none" stroke="#111" stroke-width="1.6"/></svg>
      Add Image
      <svg width="42" height="12" viewBox="0 0 42 12"><circle cx="6" cy="6" r="4" fill="none" stroke="#111" stroke-width="1.6"/><line x1="10" y1="6" x2="42" y2="6" stroke="#111" stroke-width="1.2"/></svg>
    </h1>
    <div class="browse-list">
      <div class="browse-field active"><span>Browse image 1</span><b>+</b></div>
      <div class="browse-field"><span>Browse image 2</span><b>+</b></div>
      <div class="browse-field"><span>Browse image 3</span><b>+</b></div>
    </div>
    <div class="add-more">ADD MORE +</div>
    <div class="thumbs">
      <div class="thumb thumb-foliage" role="img" aria-label="Uploaded photo: close-up of green foliage with a glowing light">
        <svg width="22" height="22" viewBox="0 0 22 22"><rect x="1.5" y="3.5" width="19" height="15" rx="2" fill="none" stroke="#fff" stroke-width="1.5"/><circle cx="7" cy="8.5" r="1.8" fill="#fff"/><path d="M3 17l5.5-5.5 3.5 3.5 3-3 4 5" fill="none" stroke="#fff" stroke-width="1.5"/></svg>
      </div>
      <div class="thumb thumb-cards" role="img" aria-label="Uploaded photo: illustrated greeting cards laid out on a table">
        <svg width="22" height="22" viewBox="0 0 22 22"><rect x="1.5" y="3.5" width="19" height="15" rx="2" fill="none" stroke="#fff" stroke-width="1.5"/><circle cx="7" cy="8.5" r="1.8" fill="#fff"/><path d="M3 17l5.5-5.5 3.5 3.5 3-3 4 5" fill="none" stroke="#fff" stroke-width="1.5"/></svg>
      </div>
      <div class="thumb thumb-tree" role="img" aria-label="Uploaded image: pink card with a swirling tree illustration">
        <svg width="22" height="22" viewBox="0 0 22 22"><rect x="1.5" y="3.5" width="19" height="15" rx="2" fill="none" stroke="#fff" stroke-width="1.5"/><circle cx="7" cy="8.5" r="1.8" fill="#fff"/><path d="M3 17l5.5-5.5 3.5 3.5 3-3 4 5" fill="none" stroke="#fff" stroke-width="1.5"/></svg>
      </div>
    </div>
    <div class="actions">
      <div class="btn btn-cancel">Cancel</div>
      <div class="btn btn-ok">OK</div>
    </div>
  </section>
</body>
</html>
```